Meridel Financial Professional Brochure

Create a professional brochure for my financial planning team, "Meridel Financial & Insurance Solutions." Please use attached logo, attached photo's and contact information for team members, menu of services, and process. Please also leave space to add a QR code later.

```html
<!DOCTYPE html>
<html lang="en">
<head>
<meta charset="utf-8">
<title>Meridel Financial Brochure</title>
<link href="https://fonts.googleapis.com/css2?family=Lato:wght@300;400;700;900&display=swap" rel="stylesheet">
<style>
:root{
  --blue:#3b6fbf;
  --navy:#233f8f;
  --grey:#7f7f7f;
  --ink:#222;
  --body:#3a3a3a;
  --page:#ffffff;
  --backdrop:#ededed;
}
*{margin:0;padding:0;box-sizing:border-box}
html,body{width:833px;height:1200px;overflow:hidden;background:var(--backdrop)}
body{font-family:'Lato',sans-serif;color:var(--body)}
.stage{position:absolute;left:0;top:0;width:960px;height:1383px;transform:scale(.8677);transform-origin:0 0}
.sheet{position:absolute;left:56px;width:848px;height:600px;background:var(--page);overflow:hidden;box-shadow:0 1px 4px rgba(0,0,0,.12)}
.sheet-outside{top:57px}
.sheet-inside{top:714px}
.sheet-art{position:absolute;left:0;top:0;width:848px;height:600px}
.section-title{position:absolute;font-size:18px;font-weight:700;white-space:nowrap}
.section-title.on-dark{color:#fff}
.section-title.on-light{color:var(--ink)}
.section-title.accent{color:var(--blue)}
.service-list{position:absolute;list-style:none;width:248px}
.service-list li{position:relative;padding-left:14px;font-size:9px;font-weight:400;line-height:12px;margin-bottom:12.4px}
.service-list li::before{content:"";position:absolute;left:0;top:4px;width:4px;height:4px;border-radius:50%;background:currentColor}
.service-list.dark li{color:var(--body)}
.service-list.light li{color:#e3ebfa}
.service-list.pale li{color:#b9d0f2}
.service-list.soft li{color:#eeeeee}
.member-photo{position:absolute;width:82px;height:92px;border-radius:8px;background:linear-gradient(160deg,#6f8fbe,#2e4b7c)}
.member{position:absolute;color:var(--ink)}
.member-name{font-size:11.5px;font-weight:700}
.member-role{font-size:10px;margin-top:1px}
.contact{display:flex;align-items:center;gap:9px;font-size:11.5px;margin-top:6px}
.contact + .contact{margin-top:2px}
.contact svg{width:11px;height:11px;flex:none}
.brand-name{position:absolute;left:598px;top:110px;width:230px;font-size:20px;font-weight:700;line-height:25px;color:var(--navy)}
.headline{position:absolute;left:34px;top:58px;font-size:37px;font-weight:900;line-height:43px;color:#111}
</style>
</head>
<body>
<div class="stage">

  <section class="sheet sheet-outside">
    <svg class="sheet-art" viewBox="0 0 848 600">
      <defs>
        <linearGradient id="checkGrad" x1="0" y1="0" x2="1" y2="0">
          <stop offset="0" stop-color="#3f74c6"/>
          <stop offset="1" stop-color="#213d92"/>
        </linearGradient>
        <linearGradient id="coverGrad" x1="0" y1="0" x2="1" y2="1">
          <stop offset="0" stop-color="#3a6cbf"/>
          <stop offset=".5" stop-color="#c9c3b8"/>
          <stop offset="1" stop-color="#5f6f86"/>
        </linearGradient>
      </defs>
      <polygon points="0,87 195,87 265,16 185,119 0,119" fill="var(--blue)"/>
      <polygon points="0,497 57,566 283,373 283,600 0,600" fill="url(#checkGrad)"/>
      <rect x="565" y="190" width="283" height="410" fill="url(#coverGrad)" role="img" aria-label="Rising arrow graphic over a photo of a desk with a calculator and financial charts"/>
    </svg>

    <h2 class="section-title on-dark" style="left:20px;top:90px">Estate Planning</h2>
    <ul class="service-list dark" style="left:20px;top:143px">
      <li>Lorem Ipsum is simply dummy text of the printing and typesetting industry.</li>
      <li>Lorem Ipsum is simply dummy text of the printing and typesetting industry.</li>
      <li>Lorem Ipsum is simply dummy text of the printing and typesetting industry.</li>
      <li>Lorem Ipsum is simply dummy text of the printing and typesetting industry.</li>
      <li>Lorem Ipsum is simply dummy text of the printing and typesetting industry.</li>
      <li>Lorem Ipsum is simply dummy text of the printing and typesetting industry.</li>
    </ul>

    <div class="member-photo" style="left:320px;top:150px" role="img" aria-label="Portrait of Dana Whitfield"></div>
    <div class="member" style="left:320px;top:255px">
      <div class="member-name">Dana Whitfield</div>
      <div class="member-role">Co-Founder &amp; CEO</div>
      <div class="contact" style="margin-top:14px">
        <svg viewBox="0 0 24 24"><path fill="#222" d="M6.6 10.8a15.1 15.1 0 0 0 6.6 6.6l2.2-2.2c.3-.3.7-.4 1-.2 1.1.4 2.3.6 3.6.6.6 0 1 .4 1 1V20c0 .6-.4 1-1 1A17 17 0 0 1 3 4c0-.6.4-1 1-1h3.5c.6 0 1 .4 1 1 0 1.3.2 2.5.6 3.6.1.3 0 .7-.2 1z"/></svg>
        <span>(555) 314 – 2790</span>
      </div>
      <div class="contact">
        <svg viewBox="0 0 24 24"><path fill="#222" d="M2 5h20v14H2z"/><path fill="none" stroke="#fff" stroke-width="1.8" d="M3 6l9 7 9-7"/></svg>
        <span>Dwhitfield@meridelguide.com</span>
      </div>
    </div>

    <div class="member-photo" style="left:320px;top:348px" role="img" aria-label="Portrait of Marcus Ibarra"></div>
    <div class="member" style="left:413px;top:365px">
      <div class="member-name">Marcus Ibarra</div>
      <div class="member-role">Chief Strategic Officer</div>
      <div class="contact" style="margin-top:12px">
        <svg viewBox="0 0 24 24"><path fill="#222" d="M6.6 10.8a15.1 15.1 0 0 0 6.6 6.6l2.2-2.2c.3-.3.7-.4 1-.2 1.1.4 2.3.6 3.6.6.6 0 1 .4 1 1V20c0 .6-.4 1-1 1A17 17 0 0 1 3 4c0-.6.4-1 1-1h3.5c.6 0 1 .4 1 1 0 1.3.2 2.5.6 3.6.1.3 0 .7-.2 1z"/></svg>
        <span>(555) 268 – 4413</span>
      </div>
    </div>

    <div class="member-photo" style="left:320px;top:470px" role="img" aria-label="Portrait of Owen Kessler"></div>
    <div class="member" style="left:413px;top:488px">
      <div class="member-name">Owen Kessler</div>
      <div class="member-role">Chief Operation Officer</div>
      <div class="contact" style="margin-top:12px">
        <svg viewBox="0 0 24 24"><path fill="#222" d="M6.6 10.8a15.1 15.1 0 0 0 6.6 6.6l2.2-2.2c.3-.3.7-.4 1-.2 1.1.4 2.3.6 3.6.6.6 0 1 .4 1 1V20c0 .6-.4 1-1 1A17 17 0 0 1 3 4c0-.6.4-1 1-1h3.5c.6 0 1 .4 1 1 0 1.3.2 2.5.6 3.6.1.3 0 .7-.2 1z"/></svg>
        <span>(555) 731 – 0586</span>
      </div>
    </div>

    <div class="brand-name">Meridel Financial &amp; Insurance Solutions</div>
  </section>

  <section class="sheet sheet-inside">
    <svg class="sheet-art" viewBox="0 0 848 600">
      <polygon points="0,300 283,90 283,600 0,600" fill="var(--blue)"/>
      <polygon points="0,303 195,303 264,231 185,333 0,333" fill="#fff"/>
      <polygon points="283,30 470,30 514,0 440,62 283,62" fill="var(--navy)"/>
      <polygon points="283,271 339,338 565,148 565,600 283,600" fill="var(--grey)"/>
      <rect x="565" y="300" width="283" height="300" fill="var(--navy)"/>
    </svg>

    <h1 class="headline">WHAT<br>WE DO</h1>

    <h2 class="section-title accent" style="left:20px;top:306px">Financial Position</h2>
    <ul class="service-list pale" style="left:20px;top:357px">
      <li>Lorem Ipsum is simply dummy text of the printing and typesetting industry.</li>
      <li>Lorem Ipsum is simply dummy text of the printing and typesetting industry.</li>
      <li>Lorem Ipsum is simply dummy text of the printing and typesetting industry.</li>
      <li>Lorem Ipsum is simply dummy text of the printing and typesetting industry.</li>
      <li>Lorem Ipsum is simply dummy text of the printing and typesetting industry.</li>
      <li>Lorem Ipsum is simply dummy text of the printing and typesetting industry.</li>
    </ul>

    <h2 class="section-title on-dark" style="left:303px;top:35px">Risk Management</h2>
    <ul class="service-list dark" style="left:303px;top:75px">
      <li>Lorem Ipsum is simply dummy text of the printing and typesetting industry.</li>
      <li>Lorem Ipsum is simply dummy text of the printing and typesetting industry.</li>
      <li>Lorem Ipsum is simply dummy text of the printing and typesetting industry.</li>
      <li>Lorem Ipsum is simply dummy text of the printing and typesetting industry.</li>
      <li>Lorem Ipsum is simply dummy text of the printing and typesetting industry.</li>
      <li>Lorem Ipsum is simply dummy text of the printing and typesetting industry.</li>
    </ul>

    <h2 class="section-title on-dark" style="left:303px;top:345px">wealth Accumulation</h2>
    <ul class="service-list soft" style="left:303px;top:376px">
      <li>Lorem Ipsum is simply dummy text of the printing and typesetting industry.</li>
      <li>Lorem Ipsum is simply dummy text of the printing and typesetting industry.</li>
      <li>Lorem Ipsum is simply dummy text of the printing and typesetting industry.</li>
      <li>Lorem Ipsum is simply dummy text of the printing and typesetting industry.</li>
      <li>Lorem Ipsum is simply dummy text of the printing and typesetting industry.</li>
      <li>Lorem Ipsum is simply dummy text of the printing and typesetting industry.</li>
    </ul>

    <h2 class="section-title on-light" style="left:585px;top:35px">Tax Management</h2>
    <ul class="service-list dark" style="left:585px;top:75px">
      <li>Lorem Ipsum is simply dummy text of the printing and typesetting industry.</li>
      <li>Lorem Ipsum is simply dummy text of the printing and typesetting industry.</li>
      <li>Lorem Ipsum is simply dummy text of the printing and typesetting industry.</li>
      <li>Lorem Ipsum is simply dummy text of the printing and typesetting industry.</li>
      <li>Lorem Ipsum is simply dummy text of the printing and typesetting industry.</li>
      <li>Lorem Ipsum is simply dummy text of the printing and typesetting industry.</li>
    </ul>

    <h2 class="section-title on-dark" style="left:585px;top:322px">Retirement Planning</h2>
    <ul class="service-list light" style="left:585px;top:362px">
      <li>Lorem Ipsum is simply dummy text of the printing and typesetting industry.</li>
      <li>Lorem Ipsum is simply dummy text of the printing and typesetting industry.</li>
      <li>Lorem Ipsum is simply dummy text of the printing and typesetting industry.</li>
      <li>Lorem Ipsum is simply dummy text of the printing and typesetting industry.</li>
      <li>Lorem Ipsum is simply dummy text of the printing and typesetting industry.</li>
      <li>Lorem Ipsum is simply dummy text of the printing and typesetting industry.</li>
    </ul>
  </section>

</div>
</body>
</html>
```